Cookie Box Packaging

We are looking for a Box for our Shortbread Cookies. They are traditional shortbread middle to high end of the market. Made with butter. We already have a successful product and would like to use the brand but not necessarily the style.

We like our design to be an mix of vintage and modern - we are open to all colours. The competition on the supermarket shelf is stiff and we need to stand out in grocery not in the gourmet food market. Our thinking is simple rather than the craziness and chaos that comes with a supermarket shelf.
Attached are some Box Ideas, created in-house, along with a black shortbread box idea , which we loved but didn't really fit into the grocery section of the supermarket. Make us stand out in the grocery shelf! I have also uploaded a logo. Our brand is not necessary but, is there if you wanted to use it. I have also uploaded our other product/packet design so you can see the brand of our other cookie which is positioned in bakery /deli not grocery.

I look forward to seeing the results

```html
<!DOCTYPE html>
<html lang="en">
<head>
<meta charset="utf-8">
<title>Shortbread Cookies – Box Front Panels</title>
<link rel="stylesheet" href="https://fonts.googleapis.com/css2?family=Montserrat:wght@300;600;800&display=swap">
<style>
  :root {
    --page: #ffffff;
    --mint: #8fd6c7;
    --lavender: #aba9ea;
    --title-white: #ffffff;
    --ink: #0b0b0b;
    --brand-pink: #e46a9c;
    --badge-navy: #1f2d4a;
    --cookie-light: #f1dca6;
    --cookie-deep: #d9b774;
    --butter: #f7e27a;
  }
  * { margin: 0; padding: 0; box-sizing: border-box; }
  html, body {
    width: 1200px; height: 1200px; overflow: hidden;
    background: var(--page);
    font-family: "Montserrat", sans-serif;
  }
  .canvas {
    position: relative; width: 1200px; height: 1200px;
    display: flex; flex-direction: column; justify-content: center; align-items: center;
    gap: 90px;
  }
  .box-front {
    position: relative; width: 1040px; height: 300px; overflow: hidden;
  }
  .box-front--mint { background: var(--mint); }
  .box-front--lavender { background: var(--lavender); }

  .brand {
    position: absolute; left: 80px; top: 44px;
    display: flex; align-items: center; gap: 8px;
    color: var(--brand-pink); font-weight: 600; font-size: 22px; letter-spacing: 0.01em;
    line-height: 1;
  }
  .brand-dot { width: 12px; height: 12px; border-radius: 50%; background: var(--brand-pink); }

  .product-photo {
    position: absolute; left: 700px; top: 34px; width: 190px; height: 230px;
    border-radius: 46% 46% 40% 40% / 30% 30% 36% 36%;
    background: radial-gradient(ellipse at 40% 35%, var(--cookie-light) 0%, var(--cookie-deep) 100%);
  }
  .product-photo::after {
    content: ""; position: absolute; right: -20px; bottom: 18px; width: 80px; height: 56px;
    border-radius: 50%;
    background: radial-gradient(circle at 40% 45%, var(--butter), #fbf1bd);
  }

  .title {
    position: absolute; left: 80px; top: 124px;
    color: var(--title-white); font-weight: 600; font-size: 62px; letter-spacing: 0.24em;
    line-height: 1; white-space: nowrap;
  }
  .subtitle {
    position: absolute; left: 86px; top: 190px;
    color: var(--ink); font-weight: 800; font-size: 42px; letter-spacing: 0.14em; line-height: 1;
  }
  .tagline {
    position: absolute; left: 88px; top: 240px;
    color: var(--title-white); font-weight: 300; font-size: 26px; letter-spacing: 0.04em; line-height: 1;
  }
  .origin-badge {
    position: absolute; right: 34px; top: 56px; width: 78px; height: 78px;
    border-radius: 50%; background: var(--badge-navy);
  }
</style>
</head>
<body>
<main class="canvas">

  <section class="box-front box-front--mint">
    <div class="brand"><span class="brand-dot"></span>Pemberly Bakes</div>
    <div class="product-photo" role="img" aria-label="Stack of three butter shortbread cookies with a curl of butter"></div>
    <h1 class="title">SHORTBREAD</h1>
    <p class="subtitle">Cookies</p>
    <p class="tagline">Made with Butter.</p>
    <div class="origin-badge" aria-hidden="true"></div>
  </section>

  <section class="box-front box-front--lavender">
    <div class="brand"><span class="brand-dot"></span>Pemberly Bakes</div>
    <div class="product-photo" role="img" aria-label="Stack of three butter shortbread cookies with a curl of butter"></div>
    <h1 class="title">SHORTBREAD</h1>
    <p class="subtitle">Cookies</p>
    <p class="tagline">Made with Butter.</p>
    <div class="origin-badge" aria-hidden="true"></div>
  </section>

</main>
</body>
</html>
```